Business Card Design

I'm a young beekeeper (22 years old) just starting out. I own and run 80 hives and would like to eventually build up to 1000. My aim is to run it in tandem with our family farm that is currently running sheep and beef. Unlike a number of honey companies on the East Coast (or the North Island, NZ) I am local and will expand onto the lease blocks that our family is also leasing. I want a simple plain logo/photo. The designer may wish to use one of the photos as a background outline or however they chose. The mountain is Moekaha and our farm borders one side of it.

Target Market(s)

From local land owners to wholesale honey buyers

Industry/Entity Type

Farm

Contact Information for Business Card

Moekaha Honey
Manager Owner Rewene Tolland
email moekahahoney@pelvanmail.co.nz
mobile 0219473061

Requirements
Must have
• The details submitted. The brand Moekaha Honey to be the main feature. The other details can be smaller.
Should not have
• Must not include a picture of a bee or hive. Use a modern font. Don't use koru but may incorporate poutama.

```html
<!DOCTYPE html>
<html lang="en">
<head>
<meta charset="utf-8">
<title>Moekaha Honey – Business Card</title>
<link rel="stylesheet" href="https://fonts.googleapis.com/css2?family=Open+Sans:wght@400;600;700&display=swap">
<style>
  :root {
    --page-bg: #e9e7e3;
    --card-bg: #f4f3ef;
    --card-shadow: rgba(0, 0, 0, 0.18);
    --honey: #f2b51c;
    --ink: #2e2e2e;
    --ink-soft: #3a3a3a;
  }
  * { box-sizing: border-box; margin: 0; padding: 0; }
  html, body {
    width: 1200px;
    height: 1000px;
    overflow: hidden;
    background: var(--page-bg);
    font-family: "Open Sans", sans-serif;
    color: var(--ink);
  }
  .stage {
    width: 1200px;
    height: 1000px;
    display: flex;
    align-items: center;
    justify-content: center;
  }
  .business-card {
    position: relative;
    width: 900px;
    height: 540px;
    background: var(--card-bg);
    box-shadow: 0 10px 30px var(--card-shadow);
  }
  .brand {
    position: absolute;
    left: 70px;
    top: 120px;
    display: flex;
    align-items: center;
    gap: 18px;
  }
  .brand-square {
    width: 46px;
    height: 46px;
    background: var(--honey);
  }
  .brand-name {
    font-size: 40px;
    font-weight: 700;
    color: var(--honey);
    letter-spacing: 0.5px;
  }
  .person {
    position: absolute;
    left: 500px;
    top: 78px;
  }
  .person-name {
    font-size: 40px;
    font-weight: 400;
    color: var(--ink);
    line-height: 1.1;
  }
  .person-role {
    font-size: 19px;
    font-weight: 600;
    color: var(--ink-soft);
    margin-left: 20px;
    margin-top: 2px;
  }
  .contact {
    position: absolute;
    left: 70px;
    bottom: 70px;
    list-style: none;
  }
  .contact-item {
    display: flex;
    align-items: center;
    gap: 16px;
    font-size: 22px;
    color: var(--ink);
    margin-top: 12px;
  }
  .contact-icon {
    width: 30px;
    height: 24px;
    flex-shrink: 0;
  }
</style>
</head>
<body>
<main class="stage">
  <section class="business-card">
    <div class="brand">
      <span class="brand-square"></span>
      <span class="brand-name">Moekaha Honey</span>
    </div>

    <div class="person">
      <p class="person-name">Rewene Tolland</p>
      <p class="person-role">Manager\Owner</p>
    </div>

    <ul class="contact">
      <li class="contact-item">
        <svg class="contact-icon" viewBox="0 0 30 24" aria-hidden="true">
          <rect x="2" y="4" width="26" height="16" fill="none" stroke="#2e2e2e" stroke-width="1.8"/>
          <polyline points="2,4 15,14 28,4" fill="none" stroke="#2e2e2e" stroke-width="1.8"/>
          <line x1="2" y1="20" x2="12" y2="11" stroke="#2e2e2e" stroke-width="1.5"/>
          <line x1="28" y1="20" x2="18" y2="11" stroke="#2e2e2e" stroke-width="1.5"/>
        </svg>
        <span>moekahahoney@pelvanmail.co.nz</span>
      </li>
      <li class="contact-item">
        <svg class="contact-icon" viewBox="0 0 30 24" aria-hidden="true">
          <path d="M9 2 C6 3 5 6 6 10 C8 16 13 21 18 22 C21 23 23 21 23 19 L19 16 L16 18 C13 16 11 13 10 10 L13 8 L11 3 Z" fill="#2e2e2e"/>
        </svg>
        <span>0219473061</span>
      </li>
    </ul>
  </section>
</main>
</body>
</html>
```